'Recalibrating Columbia' is a political thriller novel

I need a book cover for a political thriller. The book is about a presidential campaign in 2024. A politician has a revolutionary new idea on how to move the economy from growing on debt based to thriving in abundance. A billionaire oil (Brandt) family undermines his campaign with blistering negative adds. A technology billionaire attempts to assassinate him. But ultimately the incumbent president seeking a third term will not give up power...
There is an underlying theory of economics told that is meant to educate the reader about how the majority of Americans and people around the world are trying to get by in a rigged system. Although the majority of people are much worse of then they need to be the truth is nobody is winning with the current economy (unless there sinister motivations involved). The story makes dire predictions of a technological dystopia.
Updates
Author's name: Tomas Ridley
Reason: There are so many very good choices but I haven't found the perfect one yer.
Target Market(s)
Anyone who is interested in living in a better world and changing what is not working and clearly getting worse.
Industry/Entity Type
Political
Colors
Designer to choose colors to be used in the design.
Look and feel
Each slider illustrates characteristics of the customer's brand and the style your logo design should communicate.

```html
<!DOCTYPE html>
<html lang="en">
<head>
<meta charset="utf-8">
<title>Recalibrating Columbia – Cover Variants</title>
<link rel="stylesheet" href="https://fonts.googleapis.com/css2?family=Oswald:wght@700&family=Cinzel:wght@600&family=Montserrat:wght@800&display=swap">
<style>
  :root {
    --page: #ffffff;
    --ink: #000000;
    --silver: #d9d9d9;
    --vote-red: #d8202a;
    --vote-blue: #1d3fb8;
    --sun: rgba(255, 196, 60, .95);
    --marble: #e4e4e2;
  }
  * { margin: 0; padding: 0; box-sizing: border-box; }
  html, body { width: 1200px; height: 960px; overflow: hidden; background: var(--page); }
  .spread { position: relative; width: 1200px; height: 960px; }
  .cover {
    position: absolute; top: 69px; width: 590px; height: 835px;
    background: var(--ink); overflow: hidden;
  }
  .cover--color { left: 6px; }
  .cover--mono { left: 603px; }

  .art { position: absolute; }
  .art--portrait { left: 0; top: 0; width: 590px; height: 600px; }
  .art--capitol { left: 0; top: 420px; width: 590px; height: 260px; }
  .art--crowd { left: 0; top: 610px; width: 590px; height: 160px; }

  .cover--color .art--portrait {
    background:
      linear-gradient(125deg, transparent 0 52%, rgba(230,200,160,.55) 62%, rgba(140,110,80,.45) 78%, transparent 92%),
      linear-gradient(60deg, transparent 0 40%, rgba(200,80,20,.55) 50%, transparent 62%),
      radial-gradient(ellipse 160px 110px at 330px 70px, #e0742a, transparent 75%),
      linear-gradient(180deg, #2a1206 0%, #5a220a 30%, #3d1607 55%, #140703 80%, transparent 100%);
  }
  .cover--mono .art--portrait {
    background:
      linear-gradient(125deg, transparent 0 52%, rgba(235,235,235,.6) 62%, rgba(120,120,120,.45) 78%, transparent 92%),
      linear-gradient(60deg, transparent 0 40%, rgba(110,110,110,.5) 50%, transparent 62%),
      radial-gradient(ellipse 160px 110px at 330px 70px, #9a9a9a, transparent 75%),
      linear-gradient(180deg, #1a1a1a 0%, #2c2c2c 30%, #111 55%, #050505 80%, transparent 100%);
  }
  .art--capitol {
    background:
      radial-gradient(ellipse 70px 42px at 340px 205px, var(--sun), transparent 80%),
      radial-gradient(ellipse 42px 24px at 310px 150px, rgba(215,40,50,.85), transparent 80%),
      radial-gradient(ellipse 80px 120px at 300px 140px, var(--marble), transparent 75%),
      linear-gradient(180deg, transparent 0 58%, var(--marble) 72%, #bdbdbb 100%);
  }
  .art--crowd {
    background: linear-gradient(180deg, transparent 0%, rgba(0,0,0,.75) 30%, var(--ink) 55%);
  }

  .vote-badge {
    position: absolute; left: 26px; top: 21px; width: 88px; height: 88px; border-radius: 50%;
    background: linear-gradient(180deg, var(--vote-red) 0 34%, #fff 34% 66%, var(--vote-blue) 66%);
    border: 3px solid #eee; box-shadow: 0 2px 6px rgba(0,0,0,.6);
    display: flex; align-items: center; justify-content: center;
  }
  .vote-badge__label {
    font-family: 'Montserrat', sans-serif; font-weight: 800; font-size: 27px;
    color: var(--ink); letter-spacing: -0.5px;
  }
  .cover__type { position: absolute; inset: 0; width: 590px; height: 835px; }
  .title, .author {
    font-family: 'Oswald', sans-serif; font-weight: 700;
    stroke: #3a1c02; stroke-width: 2; paint-order: stroke;
  }
  .tagline { font-family: 'Cinzel', serif; font-weight: 600; }
  .star-row { fill: var(--silver); font-family: sans-serif; font-size: 26px; }
</style>
</head>
<body>
<main class="spread">
  <svg width="0" height="0" style="position:absolute" aria-hidden="true">
    <defs>
      <linearGradient id="gold" x1="0" y1="0" x2="0" y2="1">
        <stop offset="0" stop-color="#ffe27a"/>
        <stop offset="0.45" stop-color="#f2a614"/>
        <stop offset="0.55" stop-color="#c97608"/>
        <stop offset="1" stop-color="#8a4a04"/>
      </linearGradient>
    </defs>
  </svg>

  <article class="cover cover--color">
    <div class="art art--portrait" role="img" aria-label="Warm-toned photo of a man in a suit adjusting his tie, head cropped at the chin"></div>
    <div class="art art--capitol" role="img" aria-label="The Capitol building with a waving flag and a setting sun"></div>
    <div class="art art--crowd" role="img" aria-label="Cheering crowd in black silhouette with raised arms"></div>
    <div class="vote-badge"><span class="vote-badge__label">VOTE</span></div>
    <svg class="cover__type" viewBox="0 0 590 835">
      <text class="star-row" x="94" y="134" textLength="140">★★★★★</text>
      <text class="title" x="44" y="247" font-size="140" textLength="512" lengthAdjust="spacingAndGlyphs" fill="url(#gold)">RECALIBRATING</text>
      <text class="title" x="90" y="397" font-size="140" textLength="416" lengthAdjust="spacingAndGlyphs" fill="url(#gold)">COLUMBIA</text>
      <text class="star-row" x="94" y="426" textLength="140">★★★★★</text>
      <text class="tagline" x="110" y="723" font-size="24" textLength="373" fill="#e8e8e8">A POLITICAL THRILLER</text>
      <text class="author" x="132" y="799" font-size="74" textLength="326" lengthAdjust="spacingAndGlyphs" fill="url(#gold)">TOMAS RIDLEY</text>
    </svg>
  </article>

  <article class="cover cover--mono">
    <div class="art art--portrait" role="img" aria-label="Black-and-white photo of a man in a suit adjusting his tie, head cropped at the chin"></div>
    <div class="art art--capitol" role="img" aria-label="The Capitol building with a colour flag and a setting sun"></div>
    <div class="art art--crowd" role="img" aria-label="Cheering crowd in black silhouette with raised arms"></div>
    <div class="vote-badge"><span class="vote-badge__label">VOTE</span></div>
    <svg class="cover__type" viewBox="0 0 590 835">
      <text class="star-row" x="94" y="134" textLength="140">★★★★★</text>
      <text class="title" x="44" y="247" font-size="140" textLength="512" lengthAdjust="spacingAndGlyphs" fill="url(#gold)">RECALIBRATING</text>
      <text class="title" x="90" y="397" font-size="140" textLength="416" lengthAdjust="spacingAndGlyphs" fill="url(#gold)">COLUMBIA</text>
      <text class="star-row" x="94" y="426" textLength="140">★★★★★</text>
      <text class="tagline" x="110" y="723" font-size="24" textLength="373" fill="#e8e8e8">A POLITICAL THRILLER</text>
      <text class="author" x="132" y="799" font-size="74" textLength="326" lengthAdjust="spacingAndGlyphs" fill="url(#gold)">TOMAS RIDLEY</text>
    </svg>
  </article>
</main>
</body>
</html>
```